Small chamber of commerce in upstate new york. Need basic design to announce a new chocolate festival that will intend to bring in tourists to our area and give our local merchants exposure.

Industry/Entity Type

Chamber Of Commerce

Requirements
Must have
• (Beyond the information that has been listed on the enclosed jpeg, I would like to have some details on the reverse side that would include:)

Cooking with Chocolate Demo
Chocolate Decorating competition with Kids/Pastry Chefs
Live Music
Fudge Rocket Scooter Sprint
Lots & Lots of Chocolate!!!

More information contact info@pinevalechamber.org or call 845.555.0147.

```html
<!DOCTYPE html>
<html lang="en">
<head>
<meta charset="utf-8">
<title>Chocolate Festival</title>
<link rel="stylesheet" href="https://fonts.googleapis.com/css2?family=Arimo:wght@700&family=Cherry+Swash:wght@700&family=Roboto+Condensed:wght@400&family=Sofia&display=swap">
<style>
  :root {
    --page: #ffffff;
    --cocoa-light: #f6ece0;
    --cocoa-mid: #9a6440;
    --cocoa: #6b3f22;
    --cocoa-dark: #2e1a0e;
    --title-ink: #4a2815;
    --sky: #00a9e6;
    --text-light: #ffffff;
  }
  html, body {
    margin: 0;
    width: 1200px;
    height: 1200px;
    overflow: hidden;
    background: var(--page);
  }
  .flyer {
    position: absolute;
    left: 200px;
    top: 290px;
    width: 788px;
    height: 612px;
    overflow: hidden;
    background:
      radial-gradient(ellipse 420px 300px at 386px 240px,
        var(--cocoa-light) 0%, #d8b898 22%, var(--cocoa-mid) 50%, var(--cocoa) 75%, var(--cocoa-dark) 100%);
  }
  .flyer__bands {
    position: absolute;
    inset: 0;
  }
  .flyer__title {
    position: absolute;
    margin: 0;
    text-align: center;
    white-space: nowrap;
    color: var(--title-ink);
    text-shadow: 0 2px 0 rgba(255, 240, 220, 0.5), 0 3px 6px rgba(40, 20, 8, 0.4);
  }
  .flyer__title--main {
    left: 130px;
    width: 440px;
    top: 100px;
    font-family: "Sofia", cursive;
    font-size: 78px;
    font-weight: 400;
    line-height: 1;
  }
  .flyer__title--sub {
    left: 256px;
    width: 240px;
    top: 208px;
    font-family: "Cherry Swash", serif;
    font-size: 48px;
    font-weight: 700;
    line-height: 1;
  }
  .flyer__clef {
    position: absolute;
    left: 596px;
    top: 132px;
    width: 40px;
    height: 118px;
    border-radius: 20px 20px 20px 20px / 30px 30px 26px 26px;
    background: linear-gradient(180deg, #6b3a1e, #3a1e0e);
  }
  .flyer__events {
    position: absolute;
    top: 312px;
    left: 0;
    width: 100%;
    margin: 0;
    padding: 0;
    list-style: none;
    text-align: center;
    font-family: "Arimo", Arial, sans-serif;
    font-weight: 700;
    font-size: 22px;
    line-height: 30px;
    color: var(--text-light);
  }
  .flyer__contact {
    position: absolute;
    top: 542px;
    left: 0;
    width: 100%;
    margin: 0;
    text-align: center;
    font-family: "Roboto Condensed", "Arial Narrow", sans-serif;
    font-size: 20px;
    color: var(--text-light);
  }
</style>
</head>
<body>
  <main class="flyer">
    <svg class="flyer__bands" width="788" height="612" viewBox="0 0 788 612" aria-hidden="true">
      <defs>
        <linearGradient id="footer-shade" x1="0" y1="0" x2="0" y2="1">
          <stop offset="0" stop-color="#5a341c"/>
          <stop offset="1" stop-color="#2e1a0e"/>
        </linearGradient>
      </defs>
      <polygon points="0,520 386,480 788,516 788,612 0,612" fill="url(#footer-shade)"/>
      <polygon points="0,254 386,292 788,248 788,528 386,490 0,530" fill="#ffffff"/>
      <polygon points="0,260 386,298 788,254 788,516 386,480 0,520" fill="var(--sky)"/>
    </svg>

    <h1 class="flyer__title flyer__title--main">Chocolate</h1>
    <p class="flyer__title flyer__title--sub">Festival</p>
    <div class="flyer__clef" role="img" aria-label="Chocolate treble clef ornament"></div>

    <ul class="flyer__events">
      <li>Cooking with Chocolate Demo</li>
      <li>Chocolate Decorating competition with Kids / Pastry Chefs</li>
      <li>Live Music</li>
      <li>Fudge Rocket Scooter Sprint</li>
      <li>Lots &amp; Lots of Chocolate!!!</li>
    </ul>

    <p class="flyer__contact">More information contact info@pinevalechamber.org or call 845.555.0147.</p>
  </main>
</body>
</html>
```